Letterhead Design Project

I need a simple, clean and corporate letterhead & follow-on letterhead.
The follow-on letterhead should just have the logo only.
Final File Specs:
Full Bleed Size (starting document size)
213 x 300 mm
2517 x 3544 pixels
* Finished artwork should use the full bleed dimensions for best results.
Document Trim Size (final size after being cut)
210 x 297 mm
2480 x 3508 pixels
* Please be sure to keep all text within the safe margin.
Resolution 300 DPI
Accepted file types:-
Adobe Acrobat 9 Document (*.pdf) (recommended)
Adobe Illustrator CS3 Artwork (*.ai) (recommended)
Adobe Photoshop CS3 Image (*.psd) (recommended)
Bitmap Image (*.bmp)
GIF Image (*.gif)
JPEG Image (*.jpg,*.jpeg)
Microsoft PowerPoint 2010 Document (*.ppt)
Microsoft Publisher 2010 Document (*.pub)
Microsoft Word 2010 Document (*.doc)
PCX Image (*.pcx)
PICT Image (*.pic,*.pict,*.pct)
PNG Image (*.png)
PostScript Document (*.ps)
TIF Image (*.tif,*.tiff)
Windows Enhanced Metafile (*.emf)
Windows Metafile (*.wmf)
Requirements
Must have
- My letterhead must have:-
- Logo
- ACN - 482 617 309
- address - Suite 8, 51 Hartwell Ave, Coogee, NSW 2034
- phone - (02) 8371 5926
- fax - (02) 8352 6149
- email - info@brantorguard.com.au
- web - www.brantorguard.com.au
Follow-on letterhead should have the logo only

```html
<!DOCTYPE html>
<html lang="en">
<head>
<meta charset="utf-8">
<title>Brantor Guard Letterhead</title>
<link href="https://fonts.googleapis.com/css2?family=Carlito:wght@400;700&display=swap" rel="stylesheet">
<style>
  :root {
    --paper: #ffffff;
    --canvas: #ffffff;
    --edge: #4a4a4a;
    --brand-green: #9dc83b;
    --brand-navy: #151836;
    --ink: #1e1e1e;
  }
  * { box-sizing: border-box; margin: 0; padding: 0; }
  html, body {
    width: 1200px;
    height: 1000px;
    overflow: hidden;
    background: var(--canvas);
    font-family: "Carlito", "Calibri", sans-serif;
  }
  .sheet {
    position: absolute;
    top: 102px;
    width: 562px;
    height: 796px;
    background: var(--paper);
    border: 1px solid var(--edge);
  }
  .sheet--first { left: 19px; }
  .sheet--follow-on { left: 621px; width: 561px; }

  .brand-mark {
    position: absolute;
    top: 44px;
    right: 44px;
    display: flex;
    align-items: center;
    gap: 8px;
  }
  .brand-mark__square {
    width: 26px;
    height: 26px;
    background: var(--brand-green);
    border-radius: 3px;
  }
  .brand-mark__name {
    font-weight: 700;
    font-size: 30px;
    line-height: 1;
    color: var(--brand-navy);
    letter-spacing: 0.2px;
  }

  .contact-band {
    position: absolute;
    left: 0;
    right: 0;
    bottom: 8px;
    height: 23px;
    background: var(--brand-green);
    color: var(--ink);
    font-size: 7.4px;
    line-height: 9px;
    text-align: center;
    padding-top: 2px;
  }
  .contact-band strong { font-weight: 700; }
</style>
</head>
<body>
  <section class="sheet sheet--first" aria-label="First page letterhead">
    <div class="brand-mark">
      <span class="brand-mark__square"></span>
      <span class="brand-mark__name">Brantor Guard</span>
    </div>
    <footer class="contact-band">
      <p>ACN- 482 617 309, Suite 8, 51 Hartwell Ave, Coogee, NSW 2034</p>
      <p><strong>Phone</strong>- (02) 8371 5926, <strong>Fax</strong>- (02) 8352 6149, <strong>Email</strong>- info@brantorguard.com.au, <strong>Web</strong>- www.brantorguard.com.au</p>
    </footer>
  </section>

  <section class="sheet sheet--follow-on" aria-label="Follow-on letterhead">
    <div class="brand-mark">
      <span class="brand-mark__square"></span>
      <span class="brand-mark__name">Brantor Guard</span>
    </div>
  </section>
</body>
</html>
```